Poster Design Project - Coffee Take Away

To design a contemporary, eye-grabbing poster to help us build our coffee to go business. The posters will be displayed out on the street so the message needs to be communicated in an instant. The key message to get across is 'hand-crafted coffee to go', secondary message 'from £1.95'. We have a brand guide with our company colours, logo and font-style which is attached.
Updates

Thanks to all for submitting designs.  On this occasion, we have decided to revert to our existing designer. Part of the reason for going through this process was to get a fresh perspective.  Some of the designs, whilst quite different from what we normally do, were interesting and thought-provoking.  For future projects, we will invite these specific designers through ArtHive for guaranteed work.

Target Market(s)

Commuters, people on the go. Age profile 18-45, core 25-35yrs.

Industry/Entity Type

Business

Requirements
Must have
• Colours, font and logo as per our brand guideline handbook.

```html
<!DOCTYPE html>
<html lang="en">
<head>
<meta charset="utf-8">
<title>Hand-crafted coffee to go – poster set</title>
<link href="https://fonts.googleapis.com/css2?family=Inter:wght@300;400&family=Nothing+You+Could+Do&display=swap" rel="stylesheet">
<style>
  :root {
    --page: #ffffff;
    --olive: #566424;
    --orange: #f39a1e;
    --ink: #231f20;
    --white: #ffffff;
    --stripe-tone: #5d6128;
    --stripe-tone-soft: #626029;
  }
  * { box-sizing: border-box; margin: 0; padding: 0; }
  html, body { width: 852px; height: 1200px; overflow: hidden; background: var(--page); }
  .sheet { position: relative; width: 852px; height: 1200px; }

  .poster {
    position: absolute;
    width: 377px; height: 532px;
    background: var(--olive);
    overflow: hidden;
    font-family: "Inter", Arial, sans-serif;
    font-weight: 300;
  }
  .poster--a { left: 32px;  top: 32px; }
  .poster--b { left: 439px; top: 32px; }
  .poster--c { left: 32px;  top: 596px; }
  .poster--d { left: 439px; top: 596px; }

  .line {
    position: absolute; left: 0; right: 0;
    text-align: center; line-height: 1; white-space: nowrap;
  }
  .headline-kicker { color: var(--orange); font-size: 46px; letter-spacing: 0.5px; }
  .headline-main   { color: var(--white);  font-size: 96px; letter-spacing: -1px; }
  .headline-tail   { color: var(--orange); font-size: 48px; }
  .price {
    color: var(--white);
    font-family: "Nothing You Could Do", cursive;
    font-size: 46px;
    transform: rotate(-7deg);
  }
  .price--wide { font-size: 56px; }

  /* pinstripe field, rendered as one quiet flat tone */
  .stripes {
    position: absolute;
    background: linear-gradient(90deg, var(--stripe-tone), var(--stripe-tone-soft), var(--stripe-tone));
  }
  .block { position: absolute; background: var(--ink); }

  .brand { position: absolute; left: 0; right: 0; text-align: center; color: var(--white); }
  .brand-dot {
    position: absolute; left: 50%;
    border-radius: 50%;
    background: var(--white);
  }
  .brand-name {
    position: absolute; left: 0; right: 0;
    font-family: "Inter", Arial, sans-serif;
    font-weight: 300;
    color: var(--white);
    text-align: center;
    line-height: 1;
    letter-spacing: 1px;
  }
</style>
</head>
<body>
<main class="sheet">

  <!-- Variant A: plain field -->
  <section class="poster poster--a">
    <p class="line headline-kicker" style="top:45px">hand-crafted</p>
    <p class="line headline-main" style="top:92px">coffee</p>
    <p class="line headline-tail" style="top:191px">to go</p>
    <p class="line price price--wide" style="top:255px">from £1.95</p>
    <div class="brand" style="top:0">
      <span class="brand-dot" style="top:352px;width:56px;height:56px;margin-left:-28px"></span>
      <span class="brand-name" style="top:424px;font-size:20px">THE FRESH</span>
      <span class="brand-name" style="top:453px;font-size:23px">TABLE</span>
      <span class="brand-name" style="top:483px;font-size:17px">COMPANY</span>
    </div>
  </section>

  <!-- Variant B: brand block at foot -->
  <section class="poster poster--b">
    <div class="block" style="left:93px;top:0;width:186px;height:16px"></div>
    <p class="line headline-kicker" style="top:22px">hand-crafted</p>
    <p class="line headline-main" style="top:68px">coffee</p>
    <p class="line headline-tail" style="top:164px">to go</p>
    <p class="line price price--wide" style="top:222px">from £1.95</p>
    <div class="stripes" role="img" aria-label="Fine vertical multicoloured pinstripe pattern" style="left:0;top:317px;width:93px;height:215px"></div>
    <div class="stripes" role="img" aria-label="Fine vertical multicoloured pinstripe pattern" style="left:279px;top:317px;width:98px;height:215px"></div>
    <div class="block" style="left:93px;top:317px;width:186px;height:215px"></div>
    <div class="brand" style="top:0">
      <span class="brand-dot" style="top:352px;width:56px;height:56px;margin-left:-28px"></span>
      <span class="brand-name" style="top:424px;font-size:20px">THE FRESH</span>
      <span class="brand-name" style="top:453px;font-size:23px">TABLE</span>
      <span class="brand-name" style="top:483px;font-size:17px">COMPANY</span>
    </div>
  </section>

  <!-- Variant C: brand block on top, price block at foot -->
  <section class="poster poster--c">
    <div class="stripes" role="img" aria-label="Fine vertical multicoloured pinstripe pattern" style="left:0;top:0;width:122px;height:149px"></div>
    <div class="stripes" role="img" aria-label="Fine vertical multicoloured pinstripe pattern" style="left:254px;top:0;width:123px;height:149px"></div>
    <div class="block" style="left:122px;top:0;width:132px;height:149px"></div>
    <div class="brand" style="top:0">
      <span class="brand-dot" style="top:20px;width:42px;height:42px;margin-left:-21px"></span>
      <span class="brand-name" style="top:76px;font-size:14px">THE FRESH</span>
      <span class="brand-name" style="top:95px;font-size:17px">TABLE</span>
      <span class="brand-name" style="top:117px;font-size:12px">COMPANY</span>
    </div>
    <p class="line headline-kicker" style="top:173px">hand-crafted</p>
    <p class="line headline-main" style="top:221px">coffee</p>
    <p class="line headline-tail" style="top:311px">to go</p>
    <div class="stripes" role="img" aria-label="Fine vertical multicoloured pinstripe pattern" style="left:0;top:382px;width:122px;height:150px"></div>
    <div class="stripes" role="img" aria-label="Fine vertical multicoloured pinstripe pattern" style="left:254px;top:382px;width:123px;height:150px"></div>
    <div class="block" style="left:122px;top:382px;width:132px;height:150px"></div>
    <p class="line price" style="top:404px">from</p>
    <p class="line price" style="top:446px">£1.95</p>
  </section>

  <!-- Variant D: edge stripes -->
  <section class="poster poster--d">
    <div class="stripes" role="img" aria-label="Fine vertical multicoloured pinstripe pattern" style="left:0;top:0;width:20px;height:532px"></div>
    <div class="stripes" role="img" aria-label="Fine vertical multicoloured pinstripe pattern" style="left:357px;top:0;width:20px;height:532px"></div>
    <div class="brand" style="top:0">
      <span class="brand-dot" style="top:24px;width:46px;height:46px;margin-left:-23px"></span>
      <span class="brand-name" style="top:85px;font-size:16px">THE FRESH</span>
      <span class="brand-name" style="top:107px;font-size:19px">TABLE</span>
      <span class="brand-name" style="top:132px;font-size:14px">COMPANY</span>
    </div>
    <p class="line headline-kicker" style="top:177px">hand-crafted</p>
    <p class="line headline-main" style="top:227px">coffee</p>
    <p class="line headline-tail" style="top:317px">to go</p>
    <p class="line price" style="top:404px">from</p>
    <p class="line price" style="top:446px">£1.95</p>
  </section>

</main>
</body>
</html>
```